New Stationery and envelope Design Project

I need business envelopes and stationary. I would like to have office locations on both (only Chicago address) which are Chicago (Oak Brook), Washington, Mexico City, Bogota. Of course in formats I can upload and have printed. Simple and very professional I am looking for. The return address/stationary address should be:

2870 North Fenwick Avenue
Suite 1200
Riverton, Ohio 43581

Target Market(s)

I am a consultant for larger corporations

Industry/Entity Type

Consulting

Colors

Designer to choose colors to be used in the design.

Requirements
Must have
• our address, logo, very professional and clean.
Nice to have
• the names of the cities we have offices.

```html
<!DOCTYPE html>
<html lang="en">
<head>
<meta charset="utf-8">
<title>Harlan Ridge Global – Business Envelope</title>
<link rel="stylesheet" href="https://fonts.googleapis.com/css2?family=PT+Sans:wght@400;700&family=Gelasio&display=swap">
<style>
  :root {
    --paper: #ffffff;
    --edge: #bdbdbd;
    --flap-blue: #0584db;
    --brand-blue: #1553c0;
    --address-grey: #5a5a5a;
    --recipient-grey: #666666;
  }
  html, body {
    margin: 0;
    padding: 0;
    width: 1200px;
    height: 1200px;
    overflow: hidden;
    background: var(--paper);
  }
  .canvas {
    position: relative;
    width: 1200px;
    height: 1200px;
  }
  .envelope-back {
    position: absolute;
    left: 0;
    top: 0;
  }
  .envelope-front {
    position: absolute;
    left: 74px;
    top: 466px;
    width: 1061px;
    height: 462px;
    box-sizing: border-box;
    border: 1px solid var(--edge);
    background: var(--paper);
  }
  .brand-mark {
    position: absolute;
    left: 232px;
    top: 506px;
    width: 80px;
    height: 80px;
    border-radius: 50%;
    background: var(--flap-blue);
  }
  .brand-name {
    position: absolute;
    left: 188px;
    top: 601px;
    margin: 0;
    font-family: "PT Sans", sans-serif;
    font-weight: 400;
    font-size: 19px;
    line-height: 24px;
    color: var(--brand-blue);
    letter-spacing: 0.2px;
    white-space: nowrap;
  }
  .return-address {
    position: absolute;
    left: 469px;
    top: 528px;
    margin: 0;
    font-family: "PT Sans", sans-serif;
    font-style: normal;
    font-size: 13.5px;
    line-height: 16.5px;
    color: var(--address-grey);
    letter-spacing: 0.3px;
    white-space: nowrap;
  }
  .return-address .company {
    display: block;
    font-weight: 700;
    font-size: 14px;
    color: var(--brand-blue);
    margin-bottom: 3px;
  }
  .address-window {
    position: absolute;
    left: 184px;
    top: 709px;
    width: 446px;
    height: 139px;
    box-sizing: border-box;
    border: 1px solid var(--edge);
    border-radius: 24px;
  }
  .recipient {
    position: absolute;
    left: 224px;
    top: 747px;
    margin: 0;
    font-family: "Gelasio", serif;
    font-style: normal;
    font-size: 13.5px;
    line-height: 20.5px;
    color: var(--recipient-grey);
    white-space: nowrap;
  }
</style>
</head>
<body>
<main class="canvas">
  <svg class="envelope-back" width="1200" height="1200" viewBox="0 0 1200 1200" aria-hidden="true">
    <defs>
      <filter id="flap-shadow" x="-5%" y="-20%" width="110%" height="160%">
        <feDropShadow dx="0" dy="4" stdDeviation="4" flood-color="#000" flood-opacity="0.3"/>
      </filter>
    </defs>
    <rect class="back-panel" x="46.5" y="254.5" width="1061" height="460" fill="#fff" stroke="#bdbdbd"/>
    <path class="back-flap" filter="url(#flap-shadow)"
          d="M46 254 L1107 254 L1094 268 L1094 372 Q1094 392 1074 392 L78 392 Q58 392 58 372 L58 268 Z"
          fill="var(--flap-blue)"/>
  </svg>

  <section class="envelope-front"></section>

  <div class="brand-mark" aria-hidden="true"></div>
  <p class="brand-name">HARLAN RIDGE GLOBAL</p>

  <address class="return-address">
    <span class="company">Harlan Ridge Global</span>
    2870 North Fenwick Avenue<br>
    Suite 1200<br>
    Riverton, Ohio 43581
  </address>

  <div class="address-window"></div>
  <address class="recipient">
    DANIEL REYES<br>
    2400 ELM AVE. SUITE 310<br>
    PORTLAND, OR, 97205
  </address>
</main>
</body>
</html>
```